Design a scratch lotto card

Developping 2 lottery scratch card colors of preference: gold, yellow, green and blue. Size 5x3. Name of the cards are "KOL ZIB" and ''FERTO ZIB''. I want the card to be eyecatching and some dollar signs. would also prefer no writing just the name and design

Target Market(s)

people who like gambling

Colors
0792cd
33a6d7
3276b5
fbee3e
fbed22
fece3e
fbf289
9bcb3b
fefdec

Requirements
Must have
• colors mentionned and empty blank center space where grid will go
Nice to have
• cash or gold touches

```html
<!DOCTYPE html>
<html lang="en">
<head>
<meta charset="utf-8">
<title>KOL ZIB and FERTO ZIB scratch cards</title>
<link rel="stylesheet" href="https://fonts.googleapis.com/css2?family=Archivo+Black&family=Oswald:wght@400&display=swap">
<style>
  :root {
    --blue-deep: #3276b5;
    --blue-bright: #0792cd;
    --blue-soft: #33a6d7;
    --yellow: #fbee3e;
    --yellow-strong: #fbed22;
    --gold: #fece3e;
    --yellow-pale: #fbf289;
    --green: #9bcb3b;
    --cream: #fefdec;
    --ink: #1b2433;
    --panel-grey: #e6e7e8;
    --white: #ffffff;
  }
  * { margin: 0; padding: 0; box-sizing: border-box; }
  html, body { width: 1200px; height: 960px; overflow: hidden; background: var(--white); }
  .sheet { position: relative; width: 1200px; height: 960px; }

  .card {
    position: absolute;
    width: 712px;
    height: 427px;
    overflow: hidden;
    font-family: "Archivo Black", "Arial Black", sans-serif;
  }
  .card--kol { left: 44px; top: 38px; }
  .card--ferto { left: 436px; top: 500px; }

  .card__backdrop {
    position: absolute; inset: 0;
    background:
      radial-gradient(circle at 32% 45%, var(--cream) 0%, var(--yellow-pale) 35%, var(--yellow) 70%, var(--gold) 100%);
  }

  .card__logo {
    position: absolute; left: 10px; top: 9px;
    width: 134px; height: 54px;
    background: var(--white);
    display: flex; align-items: center; justify-content: center;
    font-family: "Oswald", "Arial Narrow", sans-serif;
    font-size: 23px; color: var(--ink);
    z-index: 2;
  }

  .card__title {
    position: absolute; right: 40px; top: 38px;
    font-size: 88px; line-height: 1;
    color: var(--blue-deep);
    letter-spacing: -1px;
    white-space: nowrap;
    z-index: 3;
    text-shadow: 3px 3px 0 var(--ink), -1px -1px 0 var(--ink), 1px -1px 0 var(--ink), -1px 1px 0 var(--ink);
  }
  .card--ferto .card__title { right: 30px; }

  .card__chest {
    position: absolute; left: 58px; top: 132px;
    width: 180px; height: 92px;
    border-radius: 16px 16px 8px 8px;
    background: linear-gradient(180deg, var(--gold) 0%, #c8873a 45%, #8a5a2b 100%);
    z-index: 1;
  }

  .card__scratch {
    position: absolute; left: 332px; top: 149px;
    width: 370px; height: 263px;
    background: var(--panel-grey);
    border: 3px solid var(--green);
    border-radius: 14px;
  }

  .card__pitch { position: absolute; color: var(--blue-bright); white-space: nowrap; line-height: 1;
    z-index: 2;
    text-shadow: 2px 2px 0 var(--ink); }
  .pitch__scratch { left: 30px; top: 230px; font-size: 38px; }
  .pitch__upto { left: 20px; top: 272px; font-size: 26px; letter-spacing: -0.5px; }
  .pitch__amount { left: 72px; top: 302px; font-size: 46px; }
  .pitch__cash { left: 214px; top: 356px; font-size: 30px; }

  .card__price {
    position: absolute; left: -80px; bottom: -80px;
    width: 160px; height: 160px;
    border-radius: 50%;
    background: var(--green);
  }
  .card__price-text {
    position: absolute; left: 10px; bottom: 14px;
    font-family: "Oswald", "Arial Narrow", sans-serif;
    font-size: 42px; line-height: 1; color: var(--white);
  }
</style>
</head>
<body>
<main class="sheet">
  <section class="card card--kol" aria-label="KOL ZIB scratch card">
    <div class="card__backdrop" role="img" aria-label="Yellow sunburst with scattered gold dollar coins"></div>
    <div class="card__logo">Logo here</div>
    <h1 class="card__title">KOL ZIB</h1>
    <div class="card__chest" role="img" aria-label="Open wooden treasure chest full of gold coins"></div>
    <p class="card__pitch pitch__scratch">Scratch for</p>
    <p class="card__pitch pitch__upto">Win Up To</p>
    <p class="card__pitch pitch__amount">$200,000</p>
    <p class="card__pitch pitch__cash">Cash</p>
    <div class="card__scratch" aria-label="Scratch area"></div>
    <div class="card__price"></div>
    <span class="card__price-text">$0</span>
  </section>

  <section class="card card--ferto" aria-label="FERTO ZIB scratch card">
    <div class="card__backdrop" role="img" aria-label="Yellow sunburst with scattered gold dollar coins"></div>
    <div class="card__logo">Logo here</div>
    <h1 class="card__title">FERTO ZIB</h1>
    <div class="card__chest" role="img" aria-label="Open wooden treasure chest full of gold coins"></div>
    <p class="card__pitch pitch__scratch">Scratch for</p>
    <p class="card__pitch pitch__upto">Win Up To</p>
    <p class="card__pitch pitch__amount">$200,000</p>
    <p class="card__pitch pitch__cash">Cash</p>
    <div class="card__scratch" aria-label="Scratch area"></div>
    <div class="card__price"></div>
    <span class="card__price-text">$0</span>
  </section>
</main>
</body>
</html>
```